NimbusFern cyber security firm Website

We did our website ourselves on Joomla, it's not great. We want a wordpress based redesign. Some thing that will represent a modern cyber security firm that's aimed at solving business problems.
Https://nimbusfern.co.nz (current site)
#58427c - primary color (you'll know why when you see it's name)
Logo files can be provided. Ask for more info if you need.

We want a modern, quick to load website. Website is going to have a home - services - products - about us - blogs menu. Will need a footer menu, site map, contact page etc.
We getting Content done sperately.
Our logo is #58427c - so hoping for a light theme (or at least the top is).
While we have been specific around the color - we are not after a website that has too much of it.

Reference sites that we like :
https://www.voltaline.co.nz/ - Love the full screen real world image
https://wardvex.co.nz/ (love the real world imagry and motion)
https://www.qtr.com/us-en?lnk=m
https://redowlen.com

Please dont use :
cartoon or redered images : (Like this : https://img.stockmorra.com/free-vector/cyber-security-concept_23-2148543851.jpg?w=2000 )

Please don't use images like this : https://www.tavelundi.com/eu/blog/oil-gas/app/uploads/2020/04/116137226_s-1440x564_c.jpg - they are old and boring.

We would like to see some creativity - loading our logo into a readymade wordpress template and hitting go won't cut it.
Updates

Thanks everyone who has submitted so far. We've extended the deadline as we wanted to give everyone a chance to Re- read the brief and perhaps make some tweeks should they feel it necessary.

Target Market(s)

Mid - large enterprise, finance, insurance, utilities vertical

Industry/Entity Type

Cyber security

Coding

Coded - Design and coding required

Number of Pages Required

5+ page

Font styles to use
Other font styles liked:
• Open sans

Colors

Designer to choose colors to be used in the design.

Requirements
Must have
• Simple clear messaging, something that catches user engagement
Nice to have
• Motion of some sort, but not overdone, GDPR

```html
<!DOCTYPE html>
<html lang="en">
<head>
<meta charset="utf-8">
<title>NimbusFern – Third-Party Risk Management</title>
<link href="https://fonts.googleapis.com/css2?family=Open+Sans:wght@300;400;600;700;800&display=swap" rel="stylesheet">
<style>
:root{
  --brand:#58427c;
  --brand-dark:#4a3769;
  --ink:#1a1a1a;
  --body:#444;
  --light-bg:#f4f4f6;
  --navy:#2b3a55;
  --white:#fff;
}
*{box-sizing:border-box;margin:0;padding:0}
html,body{width:1200px;height:3013px;overflow:hidden}
body{font-family:"Open Sans",sans-serif;color:var(--body);background:var(--white);position:relative}
.wrap{position:absolute;left:120px;width:960px}
a{color:inherit;text-decoration:none}

/* hero */
.hero{position:absolute;top:0;left:0;width:1200px;height:600px;
  background:radial-gradient(circle at 60% 45%,#4d5a7a 0%,#2a3147 45%,#161a28 100%)}
.hero::after{content:"";position:absolute;left:583px;bottom:0;border:17px solid transparent;border-bottom:36px solid var(--brand);border-top:0}
.topbar{top:12px;height:25px;background:var(--brand);color:#fff;font-size:10.5px;display:flex;align-items:center;padding:0 16px;gap:10px}
.topbar .social{margin-left:auto;display:flex;gap:6px}
.topbar .social i{width:9px;height:9px;border-radius:50%;background:#fff;display:block;opacity:.85}
.nav{top:37px;height:60px;background:#fff;display:flex;align-items:center;padding:0 16px}
.logo{display:flex;align-items:center;gap:8px;color:var(--brand);font-weight:700;font-size:20px;letter-spacing:.5px}
.logo .dot{width:22px;height:22px;border-radius:50%;background:var(--brand)}
.menu{margin-left:auto;display:flex;align-items:center;gap:46px;font-size:11px;font-weight:600;color:#333;letter-spacing:.3px}
.menu .active{color:var(--brand);border-bottom:1px solid var(--brand)}
.menu .cta{background:var(--brand);color:#fff;padding:11px 20px;margin-left:-8px}
.hero-text{position:absolute;top:320px;left:0;width:1200px;text-align:center;color:#fff}
.hero-text h1{font-size:42px;font-weight:800;letter-spacing:.5px}
.hero-text h1 span{font-weight:300}
.hero-text p{font-size:14px;line-height:22px;margin-top:14px}
.btn-white{display:inline-block;background:#fff;color:var(--brand);font-size:10px;font-weight:600;padding:11px 22px;margin-top:18px}

/* intro */
.intro-title{top:668px;font-size:26px;font-weight:800;color:var(--ink);line-height:32px}
.intro-title span{display:inline-block;font-weight:300;color:var(--brand);border-bottom:2px solid var(--brand);padding-bottom:2px}
.intro-copy{top:750px;width:465px;font-size:12.3px;line-height:19.6px}
.intro-copy p{margin-bottom:19px}
.line-btn{display:inline-block;font-size:10px;font-weight:600;color:var(--brand);padding:11px 27px;border-top:1px solid var(--brand);border-bottom:1px solid var(--brand)}
.intro-photo{position:absolute;top:756px;left:612px;width:453px;height:262px;background:linear-gradient(135deg,#1c2d4a,#3e6c93 50%,#1a2238);box-shadow:15px 15px 0 var(--brand)}

/* why */
.why{position:absolute;top:1140px;left:0;width:1200px;height:361px;background:var(--light-bg)}
.why::before{content:"";position:absolute;left:583px;top:-40px;border:17px solid transparent;border-bottom:40px solid var(--light-bg);border-top:0}
.why h2{position:absolute;top:68px;width:1200px;text-align:center;font-size:40px;font-weight:800;color:var(--ink)}
.why h2 span{font-weight:300}
.why-grid{top:145px;display:flex;height:74px}
.why-grid div{flex:1;background:var(--brand);color:#fff;font-size:10.5px;font-weight:600;text-align:center;display:flex;align-items:center;justify-content:center;padding:0 18px;line-height:15px;border-right:1px solid #8c7aa8}
.why-grid div:last-child{border:0}
.why .center{position:absolute;top:249px;width:1200px;text-align:center}

/* services */
.services{position:absolute;top:1501px;left:0;width:1200px;height:561px;background:radial-gradient(ellipse at 50% 70%,#3c5f7c 0%,#2b3a55 50%,#283046 100%)}
.services h2{position:absolute;top:50px;width:1200px;text-align:center;color:#fff;font-size:40px;font-weight:800}
.cards{top:135px;display:flex;gap:24px}
.card{width:222px;background:#fff}
.card .img{height:224px}
.card h3{height:53px;display:flex;align-items:center;padding:0 14px;font-size:13px;font-weight:700;color:var(--brand);line-height:15px}
.card.on h3{background:var(--brand);color:#fff}
.arrow{position:absolute;top:240px;color:#fff;font-size:20px}
.services .center{position:absolute;top:452px;width:1200px;text-align:center}
.line-btn.white{color:#fff;border-color:#fff}

/* partners */
.partners{top:2118px;display:flex}
.partner{flex:1;text-align:center;border-right:2px solid #9b8db4;height:90px;position:relative}
.partner:last-child{border:0}
.partner .badge{position:absolute;left:50%;top:0;transform:translateX(-50%)}
.partner .label{position:absolute;bottom:-16px;width:100%;font-size:13px;color:var(--brand);letter-spacing:.3px}

/* blogs */
.blogs{position:absolute;top:2287px;left:0;width:1200px;height:411px;background:var(--light-bg)}
.blogs::before{content:"";position:absolute;left:583px;top:-40px;border:17px solid transparent;border-bottom:40px solid var(--light-bg);border-top:0}
.blogs h2{position:absolute;top:68px;width:1200px;text-align:center}
.blogs h2 span{font-size:40px;font-weight:800;color:var(--ink);border-bottom:2px solid var(--brand);padding:0 2px 4px}
.posts{top:153px;display:flex;gap:24px}
.post{width:468px;height:183px;display:flex;background:#fff}
.post .img{width:187px;height:183px}
.post .txt{padding:24px 20px;font-size:11px;line-height:18px}
.post .date{font-size:10.5px}
.post h3{font-size:15px;font-weight:800;color:var(--ink);margin:6px 0 4px}
.post .more{display:inline-block;margin-top:6px;font-size:10px;color:var(--brand)}
.post.purple{background:var(--brand);color:#fff}
.post.purple h3,.post.purple .more{color:#fff}

/* footer */
.footer{position:absolute;top:2698px;left:0;width:1200px;height:315px;background:linear-gradient(135deg,#5d4784,#4c3a6e);color:#fff}
.fcols{top:40px;display:flex}
.fcol{width:246px;font-size:12.5px}
.fcol h4{font-size:17px;font-weight:700;line-height:22px;margin-bottom:16px}
.fcol li{list-style:none;line-height:25.5px}
.fcol li::before{content:"› ";}
.info{display:flex;align-items:center;gap:14px;line-height:29px}
.info .phone{font-size:15px;font-weight:600;text-decoration:underline}
.socials{display:flex;gap:8px;margin-top:20px}
.socials span{width:36px;height:36px;border:1px solid #fff;display:flex;align-items:center;justify-content:center}
.socials span.on{background:#fff}
.socials span i{width:10px;height:10px;border-radius:50%;background:#fff}
.socials span.on i{background:var(--brand)}
.news{display:flex;background:#fff;height:36px;width:222px;align-items:center;padding-left:12px;color:#666;font-size:11px;margin-top:8px}
.news b{margin-left:auto;width:28px;height:28px;margin-right:4px;background:#a99bc1;color:#fff;display:flex;align-items:center;justify-content:center;font-weight:400}
.fbottom{top:290px;display:flex;font-size:11px}
.fbottom .links{margin-left:auto}
</style>
</head>
<body>

<section class="hero">
  <div role="img" aria-label="Photo of hands typing on a laptop with floating security icons" style="position:absolute;inset:0;background:linear-gradient(160deg,rgba(70,80,110,.5),rgba(30,25,45,.6))"></div>
  <div class="wrap topbar">
    <svg width="11" height="11" viewBox="0 0 24 24" fill="none" stroke="#fff" stroke-width="2"><path d="M5 3h4l2 5-3 2a11 11 0 0 0 6 6l2-3 5 2v4a2 2 0 0 1-2 2A17 17 0 0 1 3 5a2 2 0 0 1 2-2"/></svg>
    <span>+64 (0) 210 555 0142 &nbsp;|</span>
    <svg width="11" height="11" viewBox="0 0 24 24" fill="none" stroke="#fff" stroke-width="2"><rect x="3" y="5" width="18" height="14"/><path d="M3 5l9 8 9-8"/></svg>
    <span style="text-decoration:underline">INFO@NIMBUSFERN.CO.NZ</span><span>|</span>
    <svg width="11" height="11" viewBox="0 0 24 24" fill="none" stroke="#fff" stroke-width="2"><circle cx="12" cy="12" r="9"/><path d="M12 7v5l3 2"/></svg>
    <span>MON - FRI 8AM - 5PM</span>
    <div class="social"><i></i><i></i><i></i><i></i></div>
  </div>
  <nav class="wrap nav">
    <div class="logo"><span class="dot"></span>NIMBUSFERN</div>
    <div class="menu">
      <a class="active">HOME</a><a>SERVICES ⌄</a><a>PRODUCTS ⌄</a><a>ABOUT US</a><a>BLOGS</a><a class="cta">CONTACT US</a>
    </div>
  </nav>
  <div class="hero-text">
    <h1>THIRD-PARTY RISK <span>MANAGEMENT</span></h1>
    <p>We provide the full detail, providing a multidimensional view of your entire attack<br>surface from a technical, financial impact and a compliance perspective.</p>
    <a class="btn-white">CONSULT NOW!</a>
  </div>
</section>

<h2 class="wrap intro-title">THE TECH YOU USE TO RUN YOUR BUSINESS COULD BE USED TO<br><span>SABOTAGE IT!</span></h2>
<div class="wrap intro-copy">
  <p>In the course of doing business, your company could deal with dozens of third-party vendors: suppliers, manufacturers, service providers, affiliate offices, distributors, resellers, agents, contractors, the list goes on … all of whom, in turn, deal with dozens of their own vendors. It's easy to see then why third-party cyber risk management is becoming such a high priority for businesses that deal with confidential data. (Lawyers, accountants, insurers, to name just three.)</p>
  <p>NimbusFern is a 100% New Zealand owned and operated cyber security company, designed to protect your business against exactly this kind of risk by offering third-party risk management and cyber security solutions.</p>
  <p>In short, offering small and medium sized businesses the same standard of cyber security as a large organisations – at a price that makes sense.</p>
  <a class="line-btn">ABOUT US</a>
</div>
<div class="intro-photo" role="img" aria-label="Photo of security analysts working at monitors in an operations room"></div>

<section class="why">
  <h2>WHY CHOOSE <span>US</span></h2>
  <div class="wrap why-grid">
    <div>REDUCE YOUR THIRD-PARTY RISK MANAGEMENT FROM WEEKS TO HOURS</div>
    <div>GET THE FULL VENDOR RISK VIEW ACROSS YOUR WHOLE SUPPLY CHAIN</div>
    <div>CALCULATE, CONTINUOUSLY MONITOR AND REDUCE YOUR CYBER SECURITY RISK</div>
    <div>SAVE TIME AND RESOURCES IN CYBER RISK ASSESSMENTS</div>
    <div>EXTREMELY COMPETITIVE PRICING</div>
  </div>
  <div class="center"><a class="line-btn">CONTACT US</a></div>
</section>

<section class="services">
  <h2>OUR SERVICES</h2>
  <span class="arrow" style="left:96px">‹</span><span class="arrow" style="left:1094px">›</span>
  <div class="wrap cards">
    <div class="card"><div class="img" role="img" aria-label="Photo of a person reviewing documents at a desk" style="background:linear-gradient(160deg,#8a93a8,#4b5a78)"></div><h3>CYBER SECURITY WARRANT OF FITNESS</h3></div>
    <div class="card on"><div class="img" role="img" aria-label="Photo of a hand holding a tablet with assessment icons" style="background:linear-gradient(160deg,#3f6f9c,#1d2f4f)"></div><h3>CYBER SECURITY ASSESSMENTS</h3></div>
    <div class="card"><div class="img" role="img" aria-label="Photo of hands typing on a laptop with security icons" style="background:linear-gradient(160deg,#4d5a7a,#1e2436)"></div><h3>THIRD-PARTY RISK MANAGEMENT</h3></div>
    <div class="card"><div class="img" role="img" aria-label="Photo of colleagues in a bright office meeting" style="background:linear-gradient(160deg,#c8a486,#6b5a55)"></div><h3>HUMAN RISK MANAGEMENT</h3></div>
  </div>
  <div class="center"><a class="line-btn white">VIEW ALL</a></div>
</section>

<div class="wrap partners">
  <div class="partner"><svg class="badge" width="82" height="82"><circle cx="41" cy="41" r="40" fill="#2e2e33"/></svg><div class="label">100% NZ OWNED &amp; OPERATED</div></div>
  <div class="partner"><svg class="badge" width="80" height="80" viewBox="0 0 80 80" fill="none" stroke="#333" stroke-width="3"><path d="M22 36a12 12 0 0 1 22-8a10 10 0 0 1 16 8"/><rect x="10" y="42" width="40" height="26" rx="2"/><path d="M6 72h48"/><circle cx="62" cy="54" r="9"/><circle cx="62" cy="54" r="3"/></svg><div class="label">CLOUD ONLY</div></div>
  <div class="partner"><div class="badge" style="top:26px;font-size:22px;font-weight:700;color:#222;letter-spacing:3px;white-space:nowrap">REDOWLEN</div><div class="label">ONLY NZ REDOWLEN PARTNER</div></div>
  <div class="partner"><div class="badge" style="top:22px;font-size:20px;font-weight:700;color:#222;white-space:nowrap">CORVANE</div><div class="label">CORVANE PARTNER</div></div>
</div>

<section class="blogs">
  <h2><span>BLOGS</span></h2>
  <div class="wrap posts">
    <article class="post">
      <div class="img" role="img" aria-label="Illustration of a red padlock over ransomware code" style="background:linear-gradient(160deg,#c02020,#5a0a0a)"></div>
      <div class="txt"><div class="date">15. NOV 2022</div><h3>RANSOMWARE PREVENTION</h3><b>Ransomware</b> is a type of malware from cryptovirology that threatens to publish the victim's personal data or perpetually block access to it unless a ransom is paid.<br><a class="more">READ MORE →</a></div>
    </article>
    <article class="post purple">
      <div class="img" role="img" aria-label="Photo of a team gathered around a laptop in an office" style="background:linear-gradient(160deg,#c9a684,#6f5e57)"></div>
      <div class="txt"><div class="date">14. NOV 2022</div><h3>CYBER THREAT ASSESSMENT</h3>Our pragmatic 3 step assessment will help you understand where your business may have weak controls or being targeted by malicious actors, and we will provide a strategy...<br><a class="more" style="text-decoration:underline">READ MORE →</a></div>
    </article>
  </div>
</section>

<footer class="footer">
  <div class="wrap fcols">
    <div class="fcol">
      <h4>CONTACT INFO</h4>
      <div class="info"><svg width="14" height="14" viewBox="0 0 24 24" fill="none" stroke="#fff" stroke-width="2"><path d="M5 3h4l2 5-3 2a11 11 0 0 0 6 6l2-3 5 2v4a2 2 0 0 1-2 2A17 17 0 0 1 3 5a2 2 0 0 1 2-2"/></svg><span class="phone">+64 (0) 210 555 0142</span></div>
      <div class="info"><svg width="14" height="14" viewBox="0 0 24 24" fill="none" stroke="#fff" stroke-width="2"><rect x="3" y="5" width="18" height="14"/><path d="M3 5l9 8 9-8"/></svg>info@nimbusfern.co.nz</div>
      <div class="info"><svg width="14" height="14" viewBox="0 0 24 24" fill="none" stroke="#fff" stroke-width="2"><circle cx="12" cy="12" r="9"/><path d="M12 7v5l3 2"/></svg>Mon - Fri 8am - 5pm</div>
      <div class="socials"><span><i></i></span><span class="on"><i></i></span><span><i></i></span><span><i></i></span></div>
    </div>
    <div class="fcol"><h4>QUICK LINKS</h4><ul><li><u>Home</u></li><li>About Us</li><li>Products</li><li>Blogs</li><li>Contact Us</li></ul></div>
    <div class="fcol"><h4>OUR SERVICES</h4><ul><li>Virtual CISO</li><li>Cyber Security Assessments</li><li>Third-party Risk Management</li><li>Human Risk Management</li><li>Cyber Security Warrant of Fitness</li></ul></div>
    <div class="fcol"><h4>SUBSCRIBE TO OUR<br>NEWSLETTER</h4><div class="news">Enter Your Email...<b>→</b></div></div>
  </div>
  <div class="wrap fbottom"><span>© 2022 NimbusFern Ltd. All Rights Reserved.</span><span class="links">Terms &amp; Conditions &nbsp;| &nbsp;Privacy &nbsp;| &nbsp;Cookies Policy &nbsp;| &nbsp;GDPR</span></div>
</footer>

</body>
</html>
```